Manpower and Recruitment advertisement

We are recruitment company and we need to make some creative design to explain our business to the customers , The idea which we want to deliver is ( an employee among bucklers that indicate the process of work and this employee is the one who is completing the operation of the bucklers )
I attached one photo, which has been designed before for the same concept, but we are looking for more professional and creative design

We need to show that the human being or the Manpower is the essential thing in the work process and operation . This is what we provide in our company ( The right person in the right place )

The idea will be written along with the design is :
" The right person in the right place "
Updates

Target Market(s)

The market is Saudi Arabia

Industry/Entity Type

Business

Font styles to use
Sans Serif

Requirements
Must have
• Creative idea to state the description
Nice to have
• If you have different idea that what I mentioned in the description , I would like to see your creativity

```html
<!DOCTYPE html>
<html lang="ar">
<head>
<meta charset="utf-8">
<title>Rafeeq Recruitment Company</title>
<link rel="stylesheet" href="https://fonts.googleapis.com/css2?family=Cairo:wght@400;600;700&family=Lato:wght@400;700&display=swap">
<style>
  :root {
    --sky-light: #f3dccd;
    --sky-warm: #e7b3a4;
    --suit-dark: #2a1418;
    --cape-red: #8e1420;
    --cape-deep: #5e0a12;
    --ribbon: #ef5a64;
    --ribbon-shade: #c93c48;
    --brand-pink: #d7848d;
    --brand-line: #e6aab0;
    --white: #ffffff;
    --icon: #e0707a;
  }
  * { margin: 0; padding: 0; box-sizing: border-box; }
  html, body { width: 1200px; height: 720px; overflow: hidden; background: var(--white); }
  .poster { position: relative; width: 1200px; height: 720px; overflow: hidden; }
  .hero-photo {
    position: absolute; inset: 0;
    background:
      radial-gradient(ellipse 280px 520px at 430px 380px, rgba(42,20,24,0.92), rgba(42,20,24,0) 75%),
      linear-gradient(90deg, var(--sky-light) 0%, var(--sky-warm) 22%, #b05860 40%, var(--cape-red) 62%, var(--cape-deep) 100%);
  }
  .brand { position: absolute; left: 802px; top: 40px; width: 300px; text-align: center; }
  .brand-name {
    font-family: "Cairo", sans-serif; font-weight: 700; font-size: 88px; line-height: 130px;
    color: var(--brand-pink);
  }
  .brand-rule { height: 4px; background: var(--brand-line); margin-top: 4px; }
  .brand-ar {
    font-family: "Cairo", sans-serif; font-weight: 600; font-size: 24px; line-height: 36px;
    color: var(--brand-pink); margin-top: 6px;
  }
  .brand-en {
    font-family: "Lato", sans-serif; font-size: 14px; letter-spacing: 2.2px; color: var(--brand-line);
    line-height: 18px;
  }
  .ribbon { position: absolute; left: 0; top: 0; }
  .ribbon-text { font-family: "Cairo", sans-serif; font-weight: 600; font-size: 32px; fill: var(--white); }
  .contacts { position: absolute; left: 800px; top: 546px; list-style: none; }
  .contacts li {
    display: flex; align-items: center; height: 45px;
    font-family: "Lato", sans-serif; font-size: 26px; color: var(--white);
  }
  .contacts svg { width: 34px; height: 30px; margin-right: 18px; }
</style>
</head>
<body>
<main class="poster">
  <div class="hero-photo" role="img" aria-label="Businessman in a dark suit with arms crossed and a red superhero cape flowing behind him, city skyline at sunset"></div>

  <header class="brand">
    <div class="brand-name">رفيق</div>
    <div class="brand-rule"></div>
    <div class="brand-ar">شركة رفيق للإستقدام</div>
    <div class="brand-en">RAFEEQ RECRUITMENT COMPANY</div>
  </header>

  <svg class="ribbon" width="1200" height="720" viewBox="0 0 1200 720" aria-hidden="false">
    <polygon points="736,280 820,294 792,324 788,376 732,338 754,310" fill="var(--ribbon-shade)"/>
    <polygon points="1116,470 1170,478 1148,505 1166,534 1112,518" fill="var(--ribbon-shade)"/>
    <polygon points="792,324 1116,376 1112,428 788,376" fill="var(--ribbon)"/>
    <polygon points="788,388 1116,440 1112,506 788,456" fill="var(--ribbon)"/>
    <text class="ribbon-text" x="955" y="385" text-anchor="middle" direction="rtl" transform="rotate(9 955 375)">الشخص المناسب</text>
    <text class="ribbon-text" x="950" y="460" text-anchor="middle" direction="rtl" transform="rotate(9 950 450)">في المكان المناسب</text>
  </svg>

  <ul class="contacts">
    <li>
      <svg viewBox="0 0 34 30" aria-hidden="true"><path d="M8 3 L13 8 L10 12 Q13 19 20 22 L24 19 L29 24 L25 28 Q12 27 5 9 Z" fill="none" stroke="var(--icon)" stroke-width="2.4" stroke-linejoin="round"/></svg>
      920004417
    </li>
    <li>
      <svg viewBox="0 0 34 30" aria-hidden="true"><circle cx="17" cy="15" r="12" fill="none" stroke="var(--icon)" stroke-width="2.4"/><ellipse cx="17" cy="15" rx="5" ry="12" fill="none" stroke="var(--icon)" stroke-width="2"/><line x1="5" y1="15" x2="29" y2="15" stroke="var(--icon)" stroke-width="2"/></svg>
      www.rafeeq-hr.sa
    </li>
    <li>
      <svg viewBox="0 0 34 30" aria-hidden="true"><rect x="3" y="6" width="28" height="19" fill="var(--icon)"/><polyline points="3,6 17,17 31,6" fill="none" stroke="var(--white)" stroke-width="1.6"/></svg>
      info@rafeeq-hr.sa
    </li>
  </ul>
</main>
</body>
</html>
```